Banner Ads (300X250 and 728X90)

Please create some banner ads for qvtbriefly.com in the two standard 300X250 and 728X90 pixel sizes. Each banner ad must be below 147KB in file size. Use your own creativity for designing the banners for driving traffic to qvtbriefly.com. Logo, sample banners (do not replicate or emulate, these are just FYI!), and background photo are provided. Animated .gif files are preferred.

Font styles to use
Sans Serif

Colors
f78f20
ffffff

Requirements
Must have
• The banner must cointain the domain (qvtbriefly.com) in small font for ad platform compliance purposes. Other optional copywriting is provided below.
Nice to have
• 30-Second Crypto News Digest
• Bullet Points Emailed Once Daily
• All Important News, Distilled By Analysts
• Best-In-Class 24 Hour News Brief
• qvtbriefly.com
• SUBSCRIBE

```html
<!DOCTYPE html>
<html lang="en">
<head>
<meta charset="UTF-8">
<title>QVT Briefly – Subscribe Banner</title>
<link rel="stylesheet" href="https://fonts.googleapis.com/css2?family=Poppins:wght@600;700&display=swap">
<style>
  :root {
    --brand-orange: #f78f20;
    --orange-deep: #d9731a;
    --orange-light: #fbb56a;
    --sand: #f3c79a;
    --flag-red: #c0392b;
    --white: #ffffff;
  }
  * { margin: 0; padding: 0; box-sizing: border-box; }
  html, body { width: 1200px; height: 148px; overflow: hidden; background: var(--white); }
  .banner {
    position: relative;
    width: 1200px;
    height: 148px;
    overflow: hidden;
    font-family: "Poppins", Arial, sans-serif;
    color: var(--white);
  }
  .backdrop {
    position: absolute;
    inset: 0;
    background:
      linear-gradient(90deg, rgba(150,70,20,0.55) 0%, rgba(210,110,40,0.35) 30%, rgba(247,143,32,0.15) 55%, rgba(0,0,0,0) 70%),
      linear-gradient(90deg, var(--orange-deep) 0%, var(--brand-orange) 35%, var(--orange-light) 60%, var(--sand) 78%, #e8a57a 88%, #b85a4a 100%);
  }
  .headline {
    position: absolute;
    left: 40px;
    top: 30px;
    width: 420px;
    text-align: center;
    font-weight: 700;
    font-size: 33px;
    line-height: 40px;
    text-shadow: 0 1px 3px rgba(0,0,0,0.25);
  }
  .subscribe-button {
    position: absolute;
    left: 496px;
    top: 25px;
    width: 232px;
    height: 74px;
    border-radius: 13px;
    background: var(--brand-orange);
    border: 3px solid var(--white);
    box-shadow: 0 4px 0 var(--orange-deep), 0 6px 12px rgba(0,0,0,0.2);
    display: flex;
    align-items: center;
    justify-content: center;
    font-weight: 600;
    font-size: 36px;
    color: var(--white);
  }
  .pointer-icon {
    position: absolute;
    left: 640px;
    top: 62px;
    width: 50px;
    height: 62px;
  }
  .brand {
    position: absolute;
    right: 40px;
    top: 22px;
    width: 150px;
    text-align: center;
  }
  .brand-name {
    display: block;
    font-weight: 700;
    font-size: 58px;
    line-height: 62px;
    color: var(--white);
  }
  .brand-domain {
    display: block;
    margin-top: 8px;
    font-weight: 600;
    font-size: 18px;
    color: var(--white);
  }
</style>
</head>
<body>
  <div class="banner">
    <div class="backdrop" role="img" aria-label="Warm orange-toned photo of city buildings with a flag on the right"></div>

    <p class="headline">Bullet Points Emailed<br>Once Daily</p>

    <div class="subscribe-button">Subscribe</div>

    <svg class="pointer-icon" viewBox="0 0 50 62" aria-hidden="true">
      <circle cx="14" cy="12" r="10" fill="none" stroke="#ffffff" stroke-width="2" opacity="0.8"/>
      <path d="M11 12 v24 l-6 -5 q-4 -2 -5 2 l12 18 q3 5 9 5 h12 q8 0 9 -8 v-16 q0 -4 -4 -4 q-3 0 -4 3 v-2 q0 -4 -4 -4 q-3 0 -4 3 v-1 q0 -4 -4 -4 q-3 0 -3 3 v-14 q0 -4 -4 -4 q-3 0 -3 4 z"
            fill="#ffffff" stroke="#d9731a" stroke-width="1.5"/>
    </svg>

    <div class="brand">
      <span class="brand-name">QVT</span>
      <span class="brand-domain">qvtbriefly.com</span>
    </div>
  </div>
</body>
</html>
```